Webdesign für Arbeitsschutz
Zielgruppe
Grundlage für ein funktionierendes Beschäftigungssystem ist die Schaffung und der Erhalt sicherer und menschengerechter Arbeitsbedingungen. Ein effizienter Arbeitsschutz und eine wirksame Unfallvermeidung sind hierfür besonders wichtig, vor allem auch im Hinblick auf die Herausforderungen einer durch digitalen Wandel immer schnelleren und anspruchsvolleren Arbeitswelt. Sicherheit und Gesundheit bei der Arbeit sind deshalb wichtige Arbeitsschwerpunkte im Landesamt für Betriebe und Sozialwesen. Ziel ist es, die Beschäftigten wirksam vor Gefahren und gesundheitlichen Schädigungen zu schützen. Verlässliche gesetzliche Grundlagen und rechtssichere Rahmenbedingungen für alle Unternehmen sind dafür unerlässlich.
Das wichtigste Grundlagengesetz für den betrieblichen Arbeitsschutz ist das Arbeitsschutzgesetz (ArbSchG). Es verpflichtet den Arbeitgeber, Gesundheitsgefährdungen am Arbeitsplatz zu beurteilen und über notwendige Schutzmaßnahmen zu entscheiden. Der Arbeitgeber hat für eine funktionierende Arbeitsschutzorganisation im Betrieb zu sorgen. Dies kann besonders wirksam durch eine nachhaltige Einbindung des Arbeits- und Gesundheitsschutzes in die Strukturen und Abläufe eines Unternehmens erreicht werden.
Aufgabenstellung
Gerne eine helle Seite mit schöner integration des Logo´s in die Homepage
Ich möchte keine exakte Kopie der Internet-Seite haben, aber alle Inhalte die Lemm-Arbeitsschutz anbietet (inkl. Rückrufservice, Anbringen von Referenz-Logos, Navigationsmenü)
Die Gestaltung der Hauptseite mit Farbe sollte bitte mit den vorhandenen Logo harmonieren. Die Aufteilung wo sich die Bausteine (Rückrufservice etc.) befindet sollte übersichtlich angebracht sein.

```html
<!DOCTYPE html>
<html lang="de">
<head>
<meta charset="utf-8">
<title>Sicherwerk Arbeitsschutz Süd GmbH</title>
<link href="https://fonts.googleapis.com/css2?family=Roboto+Condensed:wght@400;700&family=Roboto:wght@400;700&display=swap" rel="stylesheet">
<style>
:root{
  --teal:#0f6577;
  --teal-dark:#0b5667;
  --teal-light:#c5dde2;
  --grey-line:#cfd2d3;
  --text:#555b5e;
  --white:#ffffff;
  --photo-light:#eceef0;
  --photo-mid:#d9d6cc;
  --photo-dark:#a9abae;
}
*{box-sizing:border-box;margin:0;padding:0}
html,body{width:1200px;height:2565px;overflow:hidden}
body{font-family:"Roboto",Arial,sans-serif;color:var(--text);background:var(--white);position:relative}
section,header,footer{position:absolute;left:0;width:1200px}
.abs{position:absolute}
.btn{position:absolute;background:var(--teal);color:var(--white);border-radius:12px;font-family:"Roboto Condensed","Arial Narrow",sans-serif;font-size:16px;display:flex;align-items:center;justify-content:center}
.sec-title{font-family:"Roboto Condensed","Arial Narrow",sans-serif;color:var(--teal);font-size:22px;font-weight:400;position:absolute;white-space:nowrap}
.bars{position:absolute;height:3px;width:182px}
.bars::before,.bars::after{content:"";position:absolute;top:0;height:3px;width:79px}
.bars::before{left:0;background:var(--grey-line)}
.bars::after{left:102px;background:var(--teal)}
.body-text{position:absolute;font-size:10px;line-height:15px;color:var(--text)}
.body-text p+p{margin-top:15px}

/* hero */
.hero{top:0;height:437px}
.hero-photo{position:absolute;inset:0;background:linear-gradient(90deg,var(--photo-light) 0%,var(--photo-light) 35%,var(--photo-mid) 65%,var(--photo-dark) 100%)}
.topbar{position:absolute;top:0;left:0;width:1200px;height:133px;background:rgba(255,255,255,.82)}
.brand{position:absolute;left:94px;top:0;width:222px;height:173px;background:var(--white);box-shadow:0 2px 6px rgba(0,0,0,.25);display:flex;flex-direction:column;align-items:center;justify-content:center;gap:10px}
.brand-square{width:18px;height:18px;background:var(--teal)}
.brand-name{font-size:11px;color:var(--teal);text-align:center;line-height:14px}
.info{position:absolute;top:12px;display:flex;align-items:center;gap:8px;font-family:"Roboto Condensed","Arial Narrow",sans-serif;font-size:9.5px;line-height:12px;color:#555}
.info .ico{width:30px;height:30px;border-radius:50%;background:#dfe1e2;display:flex;align-items:center;justify-content:center}
.nav{position:absolute;top:76px;left:364px;display:flex;gap:20px;align-items:center;font-family:"Roboto Condensed","Arial Narrow",sans-serif;font-size:16px;color:#4c5356;white-space:nowrap}
.hero-title{position:absolute;left:94px;top:206px;font-family:"Roboto Condensed","Arial Narrow",sans-serif;color:var(--teal);font-size:30px;line-height:36px}
.dots{position:absolute;top:412px;left:577px;display:flex;gap:7px}
.dots span{width:10px;height:10px;background:#9a9fa3}
.dots span.on{background:#1a9bd6}

/* intro band */
.intro{top:437px;height:299px;background:linear-gradient(90deg,var(--teal) 0%,var(--teal) 62%,#4d8e9c 82%,#c6dde1 100%);color:var(--white);text-align:center}
.intro h1{font-family:"Roboto Condensed","Arial Narrow",sans-serif;font-weight:700;font-size:22px;margin-top:40px}
.intro p{font-family:"Roboto Condensed","Arial Narrow",sans-serif;font-weight:700;font-size:11.5px;line-height:22.6px;width:1010px;margin:24px auto 0}

/* task */
.task{top:736px;height:331px}
.ticks{position:absolute;left:453px;top:86px;list-style:none;font-size:10px;line-height:22.6px}
.ticks li{display:flex;align-items:center;gap:4px}
.equipment-photo{position:absolute;left:640px;top:0;width:530px;height:300px;background:linear-gradient(135deg,#f4f1e8 0%,#ebe6d6 50%,#e2e4e3 100%)}

/* callback */
.callback{top:1067px;height:356px}
.callback-photo{position:absolute;inset:0;background:linear-gradient(90deg,#9fbcc4 0%,#b9cfd4 35%,#b8d0d6 100%)}
.callback .sec-title{left:0;width:1200px;text-align:center;top:44px}
.callback .rule{position:absolute;left:476px;top:78px;width:246px;height:1px;background:var(--white)}
.callback .lead{position:absolute;left:0;top:94px;width:1200px;text-align:center;font-family:"Roboto Condensed","Arial Narrow",sans-serif;font-size:15px;line-height:18px;color:var(--white)}
.field{position:absolute;width:206px;height:36px;background:rgba(255,255,255,.85);font-size:10px;font-style:italic;color:#888;display:flex;align-items:center;padding-left:11px}
.field.send{background:var(--teal);color:var(--white);justify-content:center;padding:0}

/* info */
.infos{top:1423px;height:372px}

/* cta */
.cta{top:1795px;height:175px;background:var(--teal);color:var(--white)}
.cta h2{position:absolute;left:91px;top:24px;font-family:"Roboto Condensed","Arial Narrow",sans-serif;font-weight:400;font-size:22px}
.cta p{position:absolute;left:91px;top:52px;font-family:"Roboto Condensed","Arial Narrow",sans-serif;font-size:15px;line-height:22px}
.cta .outline{position:absolute;left:93px;top:121px;width:170px;height:39px;border:2px solid var(--white);border-radius:10px;font-family:"Roboto Condensed","Arial Narrow",sans-serif;font-size:16px;display:flex;align-items:center;justify-content:center}

/* references */
.refs{top:1970px;height:340px}
.refs .sec-title{left:0;width:1200px;text-align:center;top:44px}
.ref{position:absolute;top:115px;width:214px;height:130px;background:var(--white);box-shadow:0 0 3px rgba(0,0,0,.2);border-bottom:3px solid var(--grey-line);display:flex;align-items:center;justify-content:center;font-family:"Roboto Condensed","Arial Narrow",sans-serif;font-weight:700;font-size:28px;color:#2b3336}
.arrow{position:absolute;top:148px;width:46px;height:46px;border-radius:50%;background:var(--teal)}

/* footer */
.foot{top:2310px;height:255px;background:linear-gradient(90deg,var(--teal) 0%,var(--teal) 55%,#3f8795 80%,#7fb0ba 100%);color:var(--white);font-family:"Roboto Condensed","Arial Narrow",sans-serif}
.foot h3{font-weight:400;font-size:20px;line-height:23px}
.foot .small{font-size:10.5px;line-height:13px}
.pill{display:inline-flex;align-items:center;justify-content:center;background:var(--white);color:var(--teal);border-radius:12px;height:24px;padding:0 10px;font-size:11px}
.foot .legal{position:absolute;left:94px;top:227px;width:1012px;border-top:1px solid rgba(255,255,255,.6);padding-top:10px;text-align:center;font-size:9.5px}
</style>
</head>
<body>

<header class="hero">
  <div class="hero-photo" role="img" aria-label="Foto: Handwerker hält einen Schutzhelm und Arbeitshandschuhe, Werkzeuggürtel im Vordergrund"></div>
  <div class="topbar"></div>
  <div class="brand">
    <div class="brand-square"></div>
    <div class="brand-name">Sicherwerk Arbeitsschutz<br>Süd GmbH</div>
  </div>
  <div class="info" style="left:737px">
    <span class="ico"><svg width="14" height="16" viewBox="0 0 14 16"><circle cx="8" cy="2.5" r="2" fill="#666"/><path d="M5 6h5l-2 8h2v1H4v-1h2l1.5-6H5z" fill="#666"/></svg></span>
    <span>Hier könnte die Adresse<br>stehen wenn man möchte</span>
  </div>
  <div class="info" style="left:916px">
    <span class="ico"><svg width="14" height="14" viewBox="0 0 24 24"><path d="M6.6 10.8a15 15 0 0 0 6.6 6.6l2.2-2.2c.3-.3.7-.4 1-.2 1.1.4 2.3.6 3.6.6.6 0 1 .4 1 1V20c0 .6-.4 1-1 1A17 17 0 0 1 3 4c0-.6.4-1 1-1h3.5c.6 0 1 .4 1 1 0 1.3.2 2.5.6 3.6.1.3 0 .7-.2 1z" fill="#666"/></svg></span>
    <span>(0) 3141 20 20 20<br><span style="font-size:11.5px">info@sicherwerk-sued.de</span></span>
  </div>
  <nav class="nav">
    <svg width="20" height="18" viewBox="0 0 20 18"><path d="M10 1 1 9h3v8h5v-5h2v5h5V9h3z" fill="none" stroke="#4c5356" stroke-width="1.8"/></svg>
    <span style="margin-left:-10px">Beratung &amp; Betreuung</span><span>Seminare</span><span>E-Learning</span><span>Beauftragtenwesen</span><span>Das Unternehmen</span><span>Kontakt</span>
  </nav>
  <div class="hero-title">Mit Sicherheit<br>mehr Sicherheit</div>
  <div class="btn" style="left:94px;top:294px;width:212px;height:41px;font-size:18px">mehr Informationen</div>
  <div class="dots"><span></span><span class="on"></span><span></span></div>
</header>

<section class="intro">
  <h1>Effizienter Arbeitsschutz ist ein MUSS!</h1>
  <p>Grundlage für ein funktionierendes Beschäftigungssystem ist die Schaffung und der Erhalt sicherer und menschengerechter Arbeitsbedingungen. Ein effizienter Arbeitsschutz und eine wirksame Unfallvermeidung sind hierfür besonders wichtig, vor allem auch im Hinblick auf die Herausforderungen einer durch digitalen Wandel immer schnelleren und anspruchsvolleren Arbeitswelt. Sicherheit und Gesundheit bei der Arbeit sind deshalb wichtige Arbeitsschwerpunkte im Landesamt für Betriebe und Sozialwesen. Ziel ist es, die Beschäftigten wirksam vor Gefahren und gesundheitlichen Schädigungen zu schützen. Verlässliche gesetzliche Grundlagen und rechtssichere Rahmenbedingungen für alle Unternehmen sind dafür unerlässlich. Das wichtigste Grundlagengesetz für den betrieblichen Arbeitsschutz ist das Arbeitsschutzgesetz (ArbSchG). Es verpflichtet den Arbeitgeber, Gesundheitsgefährdungen am Arbeitsplatz zu beurteilen und über notwendige Schutzmaßnahmen zu entscheiden. Der Arbeitgeber hat für eine funktionierende Arbeitsschutzorganisation im Betrieb zu sorgen. Dies kann besonders wirksam durch eine nachhaltige Einbindung des Arbeits- und Gesundheitsschutzes in die Strukturen und Abläufe eines Unternehmens erreicht werden.</p>
</section>

<section class="task">
  <div class="equipment-photo" role="img" aria-label="Foto: Schutzhelm mit Schutzbrille, Gehörschutz und Arbeitshandschuhen"></div>
  <h2 class="sec-title" style="left:95px;top:24px">Ihre Sicherheit ist unsere Aufgabe!</h2>
  <div class="bars" style="left:95px;top:59px"></div>
  <div class="body-text" style="left:93px;top:86px;width:318px">
    <p>Lorem ipsum dolor sit amet, consetetur sadipscing elitr, sed diam nonumy eirmod tempor invidunt ut labore et dolore magna aliquyam erat, sed diam voluptua. Lorem ipsum dolor sit amet, consetetur sadipscing elitr, sed diam nonumy eirmod tempor invidunt ut labore et dolore magna aliquyam erat, sed diam voluptua.</p>
    <p>Lorem ipsum dolor sit amet, consetetur sadipscing elitr, sed diam nonumy eirmod tempor invidunt ut labore et dolore magna aliquyam erat, sed diam voluptua.</p>
  </div>
  <ul class="ticks">
    <li><svg width="11" height="9" viewBox="0 0 11 9"><path d="M1 4.5 4 7.5 10 1" fill="none" stroke="#0f6577" stroke-width="2"/></svg>Lorem ipsum dolor sit amet,</li>
    <li><svg width="11" height="9" viewBox="0 0 11 9"><path d="M1 4.5 4 7.5 10 1" fill="none" stroke="#0f6577" stroke-width="2"/></svg>Lorem ipsum dolor sit amet,</li>
    <li><svg width="11" height="9" viewBox="0 0 11 9"><path d="M1 4.5 4 7.5 10 1" fill="none" stroke="#0f6577" stroke-width="2"/></svg>Lorem ipsum dolor sit amet,</li>
    <li><svg width="11" height="9" viewBox="0 0 11 9"><path d="M1 4.5 4 7.5 10 1" fill="none" stroke="#0f6577" stroke-width="2"/></svg>Lorem ipsum dolor sit amet,</li>
    <li><svg width="11" height="9" viewBox="0 0 11 9"><path d="M1 4.5 4 7.5 10 1" fill="none" stroke="#0f6577" stroke-width="2"/></svg>Lorem ipsum dolor sit amet,</li>
    <li><svg width="11" height="9" viewBox="0 0 11 9"><path d="M1 4.5 4 7.5 10 1" fill="none" stroke="#0f6577" stroke-width="2"/></svg>Lorem ipsum dolor sit amet,</li>
  </ul>
  <div class="btn" style="left:94px;top:258px;width:171px;height:41px">mehr erfahren</div>
</section>

<section class="callback">
  <div class="callback-photo" role="img" aria-label="Hintergrundfoto: Headset auf einer Laptoptastatur, hellblau eingefärbt"></div>
  <h2 class="sec-title">Unser Rückrufservice</h2>
  <div class="rule"></div>
  <div class="lead">Lorem ipsum dolor sit amet, consetetur sadipscing elitr, sed diam nonumy<br>eirmod tempor invidunt ut labore et dolore magna aliquyam erat, sed diam</div>
  <div class="field" style="left:94px;top:159px">Anrede</div>
  <div class="field" style="left:364px;top:159px">Name</div>
  <div class="field" style="left:634px;top:159px">Vorname</div>
  <div class="field" style="left:904px;top:159px">Firma</div>
  <div class="field" style="left:94px;top:230px">Rufnummer</div>
  <div class="field" style="left:364px;top:230px">E-Mail</div>
  <div class="field" style="left:634px;top:230px">Betreff</div>
  <div class="field send" style="left:904px;top:230px">Rückruf anfordern</div>
</section>

<section class="infos">
  <h2 class="sec-title" style="left:95px;top:30px">Ein informativer Bereich</h2>
  <div class="bars" style="left:95px;top:66px"></div>
  <div class="body-text" style="left:93px;top:92px;width:380px">
    <p>Lorem ipsum dolor sit amet, consetetur sadipscing elitr, sed diam nonumy eirmod tempor invidunt ut labore et dolore magna aliquyam erat, sed diam voluptua. At vero eos et accusam et justo duo dolores et ea rebum. Stet clita kasd gubergren, no sea takimata sanctus est Lorem ipsum dolor sit amet. Lorem ipsum dolor sit amet, consetetur sadipscing elitr, sed diam nonumy eirmod tempor invidunt ut labore et dolore</p>
    <p>magna aliquyam erat, sed diam voluptua. At vero eos et accusam et justo duo dolores et ea rebum. Stet clita kasd gubergren, no sea takimata sanctus est Lorem ipsum dolor sit amet.</p>
  </div>
  <div class="btn" style="left:94px;top:286px;width:171px;height:41px">mehr erfahren</div>

  <h2 class="sec-title" style="left:634px;top:30px">Sicherheitsschuhe sind wichtig</h2>
  <div class="bars" style="left:634px;top:66px"></div>
  <div class="body-text" style="left:631px;top:92px;width:405px">
    <p>Lorem ipsum dolor sit amet, consetetur sadipscing elitr, sed diam nonumy eirmod tempor invidunt ut labore et dolore magna aliquyam erat, sed diam voluptua. At vero eos et accusam et justo duo dolores et ea rebum. Stet clita kasd gubergren, no sea takimata sanctus est Lorem ipsum dolor sit amet. Lorem ipsum dolor sit amet, consetetur sadipscing elitr, sed diam nonumy eirmod tempor invidunt ut labore et dolore</p>
    <p>magna aliquyam erat, sed diam voluptua. At vero eos et accusam et justo duo dolores et ea rebum. Stet clita kasd gubergren, no sea takimata sanctus est Lorem ipsum dolor sit amet.</p>
  </div>
  <div class="btn" style="left:632px;top:286px;width:171px;height:41px">mehr erfahren</div>
</section>

<section class="cta">
  <h2>Sie haben Fragen zum Thema Arbeitsschutz und Arbeitssicherheit?</h2>
  <p>Lorem ipsum dolor sit amet, consetetur sadipscing elitr, sed diam nonumy eirmod tempor invidunt ut labore et dolore magna aliquyam erat.<br>Lorem ipsum dolor sit amet, consetetur sadipscing elitr, sed diam nonumy.</p>
  <div class="outline">Zum Kontaktformular</div>
</section>

<section class="refs">
  <h2 class="sec-title">Unsere Referenzen</h2>
  <div class="bars" style="left:507px;top:80px"></div>
  <div class="arrow" style="left:-17px"><svg class="abs" style="left:22px;top:15px" width="10" height="16" viewBox="0 0 10 16"><path d="M9 1 2 8l7 7z" fill="#fff"/></svg></div>
  <div class="ref" style="left:136px">Sonnenquell</div>
  <div class="ref" style="left:376px">Reinwerk</div>
  <div class="ref" style="left:616px">Federlauf</div>
  <div class="ref" style="left:856px">Frachtlinie</div>
  <div class="arrow" style="left:1171px"><svg class="abs" style="left:14px;top:15px" width="10" height="16" viewBox="0 0 10 16"><path d="M1 1l7 7-7 7z" fill="#fff"/></svg></div>
</section>

<footer class="foot">
  <div class="abs" style="left:94px;top:40px;width:272px;text-align:center;font-family:'Roboto',Arial,sans-serif">
    <div style="width:22px;height:22px;background:var(--white);margin:0 auto 16px"></div>
    <div style="font-size:16px;line-height:20px">Sicherwerk Arbeitsschutz<br>Süd GmbH</div>
  </div>
  <div class="abs" style="left:399px;top:22px;width:240px">
    <h3>Sicherwerk Arbeitsschutz<br>Süd GmbH</h3>
    <div class="small" style="margin-top:16px">Max Mustermann<br>Musterstraße 123<br>123456 Musterstadt<br>Deutschland</div>
    <div class="small" style="margin-top:12px;display:flex;gap:6px">
      <svg width="9" height="9" viewBox="0 0 24 24" style="margin-top:2px"><path d="M6.6 10.8a15 15 0 0 0 6.6 6.6l2.2-2.2c.3-.3.7-.4 1-.2 1.1.4 2.3.6 3.6.6.6 0 1 .4 1 1V20c0 .6-.4 1-1 1A17 17 0 0 1 3 4c0-.6.4-1 1-1h3.5c.6 0 1 .4 1 1 0 1.3.2 2.5.6 3.6.1.3 0 .7-.2 1z" fill="#fff"/></svg>
      <span>(0812) - 44 19 30<br>(0812) - 44 19 31</span>
    </div>
  </div>
  <div class="abs" style="left:665px;top:22px">
    <h3>Menü</h3>
    <div class="small">Beratung &amp; Betreuung<br>Seminare<br>E-Learning<br>Beauftragtenwesen<br>Das Unternehmen</div>
  </div>
  <div class="abs" style="left:855px;top:18px;width:260px">
    <h3>Kontakt</h3>
    <div class="small">Für Anfragen nutzen Sie bitte unser Kontaktformular</div>
    <div class="pill" style="margin-top:6px;margin-left:-3px">Zum Kontaktformular</div>
    <h3 style="margin-top:14px">Rückrufformular</h3>
    <div class="small">Sie wünschen einen Rückruf? Dann nutzen Sie unser<br>Rückrufformular.</div>
    <div class="pill" style="margin-top:6px;margin-left:-3px">Zum Rückrufformular</div>
  </div>
  <div class="legal">© 2018 Agentur Brandlhof | Impressum | AGB | Links</div>
</footer>

</body>
</html>
```